The Dorval Lodge 5 Bedroom Cayman Islands Guest House offering weekly rentals

I am in need of a website for my 5 bedroom guest house in the Cayman Islands.
I have operated this guest house for almost three years. As the sites I am currently located on have raised their charges over the past year; I have decided to host my own site.
The site should reflect island retreat type style. With Tropical, ocean colors
Here are the core requirements I can think of.
• A comprehensive vacation rental web site
• Multiple languages if possible
• Pictures & video – of property, what’s close & the island
• Property description
• Reservation/Booking calendar.
• Information on where to go
• Social media links, such as a PalBoard & Snapgrid
• Shared moments - Event, celebration and guest photos
• Reviews page
• Rates
• Email interaction/Messaging
• Credit card processing… (Be able to securely hold the credit card information to manually process using a credit card machine (Within 24 hours)
I have already started a site on NetHarbor but got lost so once agreed I would hand over the codes as they would also be hosting the site.

Info on the house:

This spacious vacation home is a 5 minute walk away from Coral Point Public Beach and has a supermarket across the street. A small shopping plaza with a bank, pharmacy and 24 hour Hoagies is a one minute walk away. No car? No problem! The public bus stops right in front of the house, runs along Long Shell Beach and on to George Town. Take a 5 minute bus ride to Palmora Quay; an outdoor mall with restaurants, shops, Filmdome and home to the islands only observation tower.

The home boasts a fully loaded kitchen with granite counter tops, six burner gas stove, large capacity refrigerator and two dishwashers perfect for feeding a large family or group.
State of the art media room with a 73 inch high definition television, GX4, complete surround sound and plush recliners providing hours of entertainment.
Downstairs, the master suite has a comfortable memory foam king bed and an en-suite bathroom with a granite double vanity and whirlpool tub. Perfect for relaxing after a long day at the beach. Downstairs also has a cozy Queen bedroom and a serene King bedroom that shares a full bathroom. There’s an additional half-bath for added convenience.
The upstairs is a spacious double Queen bedroom and a double Full bedroom that shares a bathroom. In total the house sleeps up to 14 people very comfortably.
The screened in back porch can be accessed from the media room, downstairs Master bedroom and Queen bedroom. It’s the ideal escape to enjoy the fresh Cayman breeze without the insects.
To spare you the hassle of laundry; we’ve even provided two washers and two dryers! Leaving you more time for the beach.
For the vacation Mom, no need to worry, we have a full size crib, Tot-A-Lot Play pen, 2 full size high chairs and a car seat!

Target Market(s)

Families or groups seeking to vacation in the Caribbean or the tropics.

Industry/Entity Type

Hotel

Contact Information for Business Card

Business card front
The Dorval Lodge
Guest House
Your Cayman home away from home!
1187 Harbor View Rd, Grand Cayman, Cayman Islands
Tel: (345) 555-0147
Email: thedorvallodge@mailnest.example

Business card back
Pictures of house
5 bedroom home walking distance to the beach!
Air-conditioned, Wi-Fi, cable TV, sleeps up to 14
Book online www.thedorvallodge.example
Like us on PalBoard

Number of Pages Required

5+ page

Font styles to use
Script

Requirements
Must have
• Multiple languages if possible (English, Spanish, French)
• • Pictures & video – of property, what’s close & the island
• • Property description
• • Reservation/Booking calendar.
• • Information on where to go
• • Social media links, such as a PalBoard & Snapgrid
• • Shared moments - Event, celebration and guest photos
• • Reviews page
• • Rates
• • Email interaction/Messaging
• • Credit card processing… (Be able to securely hold the credit card information to manually process using a credit card machine (Within 24 hours)
Nice to have
• Slide show of the house on the home page
Should not have
• Too many dark colors

```html
<!DOCTYPE html>
<html lang="en">
<head>
<meta charset="utf-8">
<title>The Dorval Lodge</title>
<link rel="stylesheet" href="https://fonts.googleapis.com/css2?family=Raleway:wght@400;500;600;700&family=Great+Vibes&display=swap">
<style>
:root{
  --gold:#e1b143;
  --gold-dark:#c9952a;
  --gold-soft:#eec467;
  --ink:#222222;
  --body:#555555;
  --navy:#0f2236;
  --navy-deep:#0a1726;
  --white:#ffffff;
  --field:#9aa1aa;
}
*{margin:0;padding:0;box-sizing:border-box}
html,body{width:1200px;height:2917px;overflow:hidden}
body{font-family:"Raleway",Arial,sans-serif;color:var(--body);background:var(--white);position:relative}
section,header,footer{position:absolute;left:0;width:1200px}
.abs{position:absolute}

.topbar{top:0;height:43px;background:var(--gold);color:var(--white);font-size:13px}
.topbar .contact-line{left:99px;top:13px;display:flex;align-items:center;gap:10px}
.topbar .sep{opacity:.8;margin:0 8px}
.lang-select{left:984px;top:7px;width:116px;height:28px;background:var(--white);border:1px solid #bbb;color:var(--ink);font-size:12px;display:flex;align-items:center;padding:0 8px;gap:8px}
.lang-select .flag{width:18px;height:13px;background:#3d59a8}
.lang-select .caret{margin-left:auto;font-size:9px}

.site-nav{top:43px;height:83px;background:var(--white)}
.brand{left:99px;top:28px;font-size:24px;font-weight:600;color:var(--ink)}
.menu{top:33px;font-size:15px;color:var(--ink);font-weight:500}
.menu.active::after{content:"";position:absolute;left:0;right:0;bottom:-12px;height:2px;background:var(--ink)}

.hero{top:126px;height:500px}
.hero-photo{left:0;top:0;width:1200px;height:480px;background:linear-gradient(180deg,#6d6a63 0%,#8a7a55 35%,#4e5a3a 70%,#3b3f33 100%)}
.hero-title{left:0;width:1200px;top:62px;text-align:center;font-family:"Great Vibes",cursive;font-size:66px;font-weight:400;color:var(--white)}
.hero-title span{color:var(--gold)}
.hero-text{left:240px;width:720px;top:180px;text-align:center;color:var(--white);font-size:14px;line-height:31px}
.slide-arrow{width:42px;height:42px;border:2px solid var(--white);border-radius:50%;top:178px}

.rooms{top:473px;height:390px}
.room-card{top:0;width:314px;height:387px;border:6px solid var(--white);text-align:center;color:var(--white);background:var(--white)}
.room-card .photo{position:absolute;inset:0}
.room-card h3{position:absolute;left:0;right:0;top:80px;font-size:26px;font-weight:700;text-transform:uppercase}
.room-card h4{position:absolute;left:0;right:0;top:140px;font-size:22px;font-weight:500;color:var(--gold)}
.room-card p{position:absolute;left:30px;right:30px;top:192px;font-size:14px;line-height:27px}
.room-card .btn{position:absolute;left:92px;top:295px;width:117px;height:39px;background:var(--gold);color:var(--white);font-size:13px;line-height:39px;text-transform:uppercase}

.welcome{top:860px;height:330px;text-align:center}
.section-title{font-size:34px;font-weight:500;color:var(--ink);left:0;width:1200px;text-align:center}
.section-title span{color:var(--gold)}
.welcome p{left:117px;width:966px;top:150px;font-size:13px;line-height:26px}
.pill{top:278px;height:40px;border-radius:20px;color:var(--white);font-size:15px;line-height:40px;text-align:center}

.gallery{top:1186px;height:525px;overflow:hidden}
.gallery-bg{inset:0;background:linear-gradient(180deg,#173449 0%,#1f3d4a 40%,#2b2c28 100%)}
.gallery .section-title{color:var(--gold);top:80px;font-size:32px}
.frame{border:7px solid var(--white)}
.round-arrow{width:40px;height:40px;border:2px solid var(--white);border-radius:50%;top:430px}

.events{top:1708px;height:380px}
.block-title{font-size:28px;font-weight:500;color:var(--ink);top:30px}
.block-title span{color:var(--gold)}
.event-photo{top:107px;width:181px;height:132px}
.event-name{top:257px;font-size:17px;color:var(--ink)}
.event-sub{top:286px;font-size:14px;color:var(--ink)}
.stars{top:308px;font-size:14px;color:#777;letter-spacing:1px}
.field{height:43px;border:1px solid #c6c6c6;background:var(--white);font-size:13px;color:var(--ink);padding:0 12px;display:flex;align-items:center}
.field .end{margin-left:auto;font-size:10px}
.date-btn{position:absolute;right:0;top:0;width:44px;height:41px;background:var(--gold)}
.book-btn{top:288px;left:739px;width:362px;height:42px;background:linear-gradient(180deg,var(--gold-soft),var(--gold-dark));color:var(--white);font-size:14px;font-weight:600;text-align:center;line-height:42px;text-transform:uppercase}

.reviews{top:2071px;height:400px;overflow:hidden}
.reviews-bg{inset:0;background:linear-gradient(180deg,#e8b646 0%,#d9a63c 50%,#c79a3a 100%)}
.reviews .section-title{color:var(--white);top:70px;font-size:32px}
.avatar{top:179px;width:106px;height:106px;border-radius:50%;border:5px solid var(--white);background:linear-gradient(180deg,#c9c2b8,#6d6358)}
.quote{top:190px;font-size:40px;color:var(--white);font-family:Georgia,serif;font-weight:700;line-height:1}
.review-name{top:218px;color:var(--white);font-size:16px;font-weight:600}
.review-role{top:245px;color:#fbe8bf;font-size:14px}
.review-text{top:294px;width:525px;color:var(--white);font-size:13px;line-height:26px}

.contact{top:2470px;height:385px;color:var(--white)}
.contact-bg{inset:0;background:linear-gradient(180deg,var(--navy) 0%,#14304a 50%,var(--navy-deep) 100%)}
.contact h2{left:99px;top:50px;font-size:28px;font-weight:600}
.contact .rule{left:99px;top:92px;width:152px;height:2px;background:var(--white)}
.info-icon{left:99px;width:46px;height:46px;border-radius:50%;border:2px solid var(--white);display:flex;align-items:center;justify-content:center}
.info-icon.filled{background:var(--gold);border-color:var(--gold)}
.info-text{left:170px;font-size:16px;font-weight:600;line-height:24px}
.form-title{left:484px;top:56px;font-size:18px;font-weight:600}
.input{background:var(--field);color:#e8ebee;font-size:13px;padding:0 10px;line-height:40px;height:40px;border:1px solid #b5bac0;opacity:.85}
.send-btn{left:484px;top:317px;width:117px;height:35px;background:var(--gold);color:var(--white);font-size:14px;font-weight:600;text-align:center;line-height:35px}

.site-footer{top:2855px;height:62px;background:var(--gold);color:var(--white)}
.copyright{left:99px;top:23px;font-size:13px}
.pay{top:18px;width:38px;height:25px;background:var(--white);border-radius:3px}
.social{top:16px;width:30px;height:30px;border:2px solid var(--white);border-radius:50%}
</style>
</head>
<body>

<header class="topbar">
  <div class="abs contact-line">
    <svg width="14" height="11" viewBox="0 0 14 11"><rect x="0.5" y="0.5" width="13" height="10" fill="none" stroke="#fff"/><path d="M1 1l6 5 6-5" fill="none" stroke="#fff"/></svg>
    <span>info@dorvallodge.example</span>
    <span class="sep">|</span>
    <svg width="12" height="12" viewBox="0 0 24 24"><path fill="#fff" d="M6.6 10.8a15 15 0 006.6 6.6l2.2-2.2a1 1 0 011-.25 11.4 11.4 0 003.6.57 1 1 0 011 1V20a1 1 0 01-1 1A17 17 0 013 4a1 1 0 011-1h3.5a1 1 0 011 1c0 1.25.2 2.45.57 3.57a1 1 0 01-.25 1z"/></svg>
    <span>+1800 555 0199</span>
  </div>
  <div class="abs lang-select"><span class="flag"></span><span>France</span><span class="caret">▼</span></div>
</header>

<header class="site-nav">
  <div class="abs brand">The Dorval Lodge</div>
  <nav>
    <span class="abs menu active" style="left:574px">Home</span>
    <span class="abs menu" style="left:669px">About Us</span>
    <span class="abs menu" style="left:788px">Our Rooms</span>
    <span class="abs menu" style="left:922px">Events</span>
    <span class="abs menu" style="left:1021px">Contact Us</span>
  </nav>
</header>

<section class="hero">
  <div class="abs hero-photo" role="img" aria-label="Photo of the yellow guest house with palm trees"></div>
  <svg class="abs" style="left:0;top:440px" width="1200" height="60" viewBox="0 0 1200 60" preserveAspectRatio="none">
    <path d="M0 45 Q600 -5 1200 45 L1200 60 L0 60Z" fill="#fff"/>
    <path d="M0 35 Q600 -15 1200 35 L1200 45 Q600 -5 0 45Z" fill="#e1b143"/>
  </svg>
  <h1 class="abs hero-title">Dorval <span>Lodge</span></h1>
  <p class="abs hero-text">Sed ut perspiciatis unde omnis iste natus error sit voluptatem accusantium doloremque laudantium, totam rem aperiam, eaque ipsa quae ab illo inventore veritatis</p>
  <div class="abs slide-arrow" style="left:24px"><svg width="38" height="38" viewBox="0 0 38 38"><path d="M21 13l-6 6 6 6" fill="none" stroke="#fff" stroke-width="2"/></svg></div>
  <div class="abs slide-arrow" style="left:1133px"><svg width="38" height="38" viewBox="0 0 38 38"><path d="M17 13l6 6-6 6" fill="none" stroke="#fff" stroke-width="2"/></svg></div>
</section>

<section class="rooms">
  <article class="abs room-card" style="left:99px">
    <div class="photo" role="img" aria-label="Photo of the master bedroom" style="background:linear-gradient(180deg,#1e3550,#14253a 60%,#2a3140)"></div>
    <h3>Master Bedroom</h3><h4>Living Room</h4>
    <p>At vero eos et accusamus et iusto odio dignissimos ducimus qui blan ditiis praesen volup.</p>
    <span class="btn">Read More</span>
  </article>
  <article class="abs room-card" style="left:443px">
    <div class="photo" role="img" aria-label="Photo of the kitchen" style="background:linear-gradient(180deg,#4a2e1c,#2d1d14 60%,#3a2a1f)"></div>
    <h3>Kitchen Room</h3><h4>Dual Dishwashers</h4>
    <p>At vero eos et accusamus et iusto odio dignissimos ducimus qui blan ditiis praesent volup.</p>
    <span class="btn">Read More</span>
  </article>
  <article class="abs room-card" style="left:788px">
    <div class="photo" role="img" aria-label="Photo of the living room" style="background:linear-gradient(180deg,#3d3024,#2a2118 60%,#403428)"></div>
    <h3>Living Room</h3><h4>Living Room</h4>
    <p>At vero eos et accusamus et iusto odio dignissimos ducimus qui blan ditiis praesen volup.</p>
    <span class="btn">Read More</span>
  </article>
</section>

<section class="welcome">
  <h2 class="abs section-title" style="top:56px">Welcome To <span>The Dorval Lodge</span></h2>
  <svg class="abs" style="left:530px;top:111px" width="140" height="14" viewBox="0 0 140 14"><line x1="0" y1="7" x2="140" y2="7" stroke="#333"/><circle cx="50" cy="7" r="4" fill="#fff" stroke="#333"/><circle cx="70" cy="7" r="4" fill="#fff" stroke="#e1b143"/><circle cx="90" cy="7" r="4" fill="#fff" stroke="#333"/></svg>
  <p class="abs">Sed ut perspiciatis unde omnis iste natus error sit voluptatem accusantium doloremque laudantium, totam rem aperiam, eaque ipsa quae ab illo inventore verita tis et quasi architecto beatae vitae dicta sunt explicabo. Nemo enim ipsam voluptatem quia voluptas sit aspernatur aut odit aut fugit sit aspernatur aut odit aut fugit. Excepteur sint occaecat cupidatat non proident, sunt in culpa qui officia deserunt mollit anim id est laborum. Excepteur sint occaecat cupidatat non proident, sunt in culpa qui officia deserunt mollit anim id est laborum.</p>
  <span class="abs pill" style="left:465px;width:120px;background:linear-gradient(180deg,#eec467,#d29d32)">Read More</span>
  <span class="abs pill" style="left:611px;width:122px;background:#3d3d3d">Contact Us</span>
</section>

<section class="gallery">
  <div class="abs gallery-bg" role="img" aria-label="Photo of a rocky coastline at dusk"></div>
  <svg class="abs" style="left:0;top:0" width="1200" height="60" viewBox="0 0 1200 60" preserveAspectRatio="none"><path d="M0 0H1200V0 Q600 80 0 0Z" fill="#fff"/></svg>
  <h2 class="abs section-title">Dorval Lodge Gallery</h2>
  <svg class="abs" style="left:530px;top:143px" width="140" height="14" viewBox="0 0 140 14"><line x1="0" y1="7" x2="140" y2="7" stroke="#e1b143"/><circle cx="50" cy="7" r="4" fill="none" stroke="#e1b143"/><circle cx="70" cy="7" r="4" fill="none" stroke="#e1b143"/><circle cx="90" cy="7" r="4" fill="none" stroke="#e1b143"/></svg>
  <div class="abs frame" style="left:99px;top:168px;width:309px;height:256px;transform:perspective(700px) rotateY(18deg);background:linear-gradient(135deg,#b9c6d2,#6f86a3 50%,#3c4e6a)" role="img" aria-label="Guest photo of a group indoors"></div>
  <div class="abs frame" style="left:445px;top:199px;width:306px;height:195px;background:linear-gradient(135deg,#4fa3a0,#2f7d6e 60%,#1f5a52)" role="img" aria-label="Video still of snorkelling underwater">
    <svg class="abs" style="left:133px;top:78px" width="28" height="28" viewBox="0 0 28 28"><circle cx="14" cy="14" r="14" fill="#fff" opacity=".85"/><path d="M11 8l9 6-9 6z" fill="#333"/></svg>
  </div>
  <div class="abs frame" style="left:788px;top:168px;width:313px;height:256px;transform:perspective(700px) rotateY(-18deg);background:linear-gradient(135deg,#57c4d8,#2b95b4 55%,#1d6c8a)" role="img" aria-label="Guest photo in clear turquoise sea"></div>
  <div class="abs round-arrow" style="left:550px"><svg width="36" height="36" viewBox="0 0 36 36"><path d="M20 12l-6 6 6 6" fill="none" stroke="#fff" stroke-width="2"/></svg></div>
  <div class="abs round-arrow" style="left:608px"><svg width="36" height="36" viewBox="0 0 36 36"><path d="M16 12l6 6-6 6" fill="none" stroke="#fff" stroke-width="2"/></svg></div>
</section>

<section class="events">
  <h2 class="abs block-title" style="left:99px">Our <span>Latest Events</span></h2>
  <div class="abs event-photo" style="left:99px;background:linear-gradient(180deg,#a9c4dc,#5c7898 60%,#7a8c9a)" role="img" aria-label="Photo of a wedding party group"></div>
  <div class="abs event-photo" style="left:311px;background:linear-gradient(180deg,#e9c79a,#c99a6a 55%,#8a6e58)" role="img" aria-label="Photo of a couple at sunset"></div>
  <div class="abs event-photo" style="left:523px;background:linear-gradient(180deg,#6a4a3a,#4a3a2e 55%,#6c5a3c)" role="img" aria-label="Photo of guests at a dinner table"></div>
  <span class="abs event-name" style="left:99px">Wedding Parties</span>
  <span class="abs event-name" style="left:311px">Wedding Parties</span>
  <span class="abs event-name" style="left:523px">Wedding Parties</span>
  <span class="abs event-sub" style="left:99px">perspiciatis unde omnis</span>
  <span class="abs event-sub" style="left:311px">perspiciatis unde omnis</span>
  <span class="abs event-sub" style="left:523px">perspiciatis unde omnis</span>
  <span class="abs stars" style="left:99px"><span style="color:#e1b143">★★★★</span>☆</span>
  <span class="abs stars" style="left:311px"><span style="color:#e1b143">★★★★</span>☆</span>
  <span class="abs stars" style="left:523px"><span style="color:#e1b143">★★★★</span>☆</span>

  <h2 class="abs block-title" style="left:739px">Book Your <span>Resort Now</span></h2>
  <div class="abs field" style="left:739px;top:107px;width:362px">Enter Email<span class="end">▼</span></div>
  <div class="abs field" style="left:739px;top:167px;width:174px">From Date<span class="date-btn"><svg width="44" height="41" viewBox="0 0 44 41"><rect x="16" y="14" width="12" height="12" fill="none" stroke="#fff"/><line x1="16" y1="17" x2="28" y2="17" stroke="#fff"/></svg></span></div>
  <div class="abs field" style="left:927px;top:167px;width:174px">To Date<span class="date-btn"><svg width="44" height="41" viewBox="0 0 44 41"><rect x="16" y="14" width="12" height="12" fill="none" stroke="#fff"/><line x1="16" y1="17" x2="28" y2="17" stroke="#fff"/></svg></span></div>
  <div class="abs field" style="left:739px;top:227px;width:362px">No of Rooms<span class="end">▼</span></div>
  <div class="abs book-btn">Book Your Resort</div>
</section>

<section class="reviews">
  <div class="abs reviews-bg" role="img" aria-label="Photo of a couple on the beach in golden tones"></div>
  <svg class="abs" style="left:0;top:0" width="1200" height="50" viewBox="0 0 1200 50" preserveAspectRatio="none"><path d="M0 0H1200V5 Q600 50 0 5Z" fill="#fff"/></svg>
  <h2 class="abs section-title">People Reviews</h2>
  <svg class="abs" style="left:530px;top:128px" width="140" height="14" viewBox="0 0 140 14"><line x1="0" y1="7" x2="140" y2="7" stroke="#fff"/><circle cx="50" cy="7" r="4" fill="#e1b143" stroke="#fff"/><circle cx="70" cy="7" r="4" fill="#e1b143" stroke="#fff"/><circle cx="90" cy="7" r="4" fill="#e1b143" stroke="#fff"/></svg>

  <div class="abs avatar" style="left:111px" role="img" aria-label="Portrait of a reviewer"></div>
  <span class="abs quote" style="left:243px">“</span>
  <span class="abs review-name" style="left:243px">The Dorval Lodge is great</span>
  <span class="abs review-role" style="left:243px">Daniel Reyes(CEO &amp; Founder)</span>
  <p class="abs review-text" style="left:99px">Neque porro quisquam est, qui dolorem ipsum quia dolor sit amet, con sec tetur, adipis civelit sed quia non qui dolorem ipsum quia dolor sit amet, con sectetur, adipis civelit. Red quia num quam eius modi.</p>

  <div class="abs avatar" style="left:651px" role="img" aria-label="Portrait of a reviewer"></div>
  <span class="abs quote" style="left:786px">“</span>
  <span class="abs review-name" style="left:786px">The Dorval Lodge is great</span>
  <span class="abs review-role" style="left:786px">Daniel Reyes(CEO &amp; Founder)</span>
  <p class="abs review-text" style="left:636px;width:465px">Neque porro quisquam est, qui dolorem ipsum quia dolor sit amet, con sec tetur, adipis civelit sed quia non qui dolorem ipsum quia dolor sit amet, con sectetur, adipis civelit. Red quia num quam eius modi.</p>
</section>

<section class="contact">
  <div class="abs contact-bg" role="img" aria-label="Dark underwater photo of a diver"></div>
  <h2 class="abs">Contact Us</h2>
  <div class="abs rule"></div>
  <div class="abs info-icon" style="top:139px"><svg width="22" height="22" viewBox="0 0 22 22"><circle cx="11" cy="11" r="9" fill="none" stroke="#fff" stroke-width="2"/><path d="M11 5v6l4 2" fill="none" stroke="#fff" stroke-width="2"/></svg></div>
  <div class="abs info-text" style="top:150px">Tuesday – Sunday 9am – 5pm EST</div>
  <div class="abs info-icon filled" style="top:216px"><svg width="18" height="22" viewBox="0 0 18 22"><path d="M9 1a7 7 0 00-7 7c0 5 7 13 7 13s7-8 7-13a7 7 0 00-7-7z" fill="none" stroke="#fff" stroke-width="2"/><circle cx="9" cy="8" r="2.5" fill="#fff"/></svg></div>
  <div class="abs info-text" style="top:216px">Harbor Coast, Palm Isles<br>Seabright.</div>
  <div class="abs info-icon" style="top:293px"><svg width="20" height="20" viewBox="0 0 24 24"><path fill="none" stroke="#fff" stroke-width="2" d="M6.6 10.8a15 15 0 006.6 6.6l2.2-2.2a1 1 0 011-.25 11.4 11.4 0 003.6.57 1 1 0 011 1V20a1 1 0 01-1 1A17 17 0 013 4a1 1 0 011-1h3.5a1 1 0 011 1c0 1.25.2 2.45.57 3.57a1 1 0 01-.25 1z"/></svg></div>
  <div class="abs info-text" style="top:304px">+1800 555 0199</div>

  <div class="abs form-title">Fill out the form below, and we'll contact you shortly.</div>
  <div class="abs input" style="left:484px;top:103px;width:290px">First Name</div>
  <div class="abs input" style="left:809px;top:103px;width:292px">Last Name</div>
  <div class="abs input" style="left:484px;top:158px;width:290px">Phone Number</div>
  <div class="abs input" style="left:809px;top:158px;width:292px">E-Mail Address</div>
  <div class="abs input" style="left:484px;top:214px;width:617px;height:84px;line-height:30px">Message</div>
  <div class="abs send-btn">Send Now</div>
</section>

<footer class="site-footer">
  <div class="abs copyright">Copyright © 2016 The Dorval Lodge - All rights reserved</div>
  <span class="abs pay" style="left:776px"></span>
  <span class="abs pay" style="left:822px"></span>
  <span class="abs pay" style="left:868px"></span>
  <span class="abs pay" style="left:914px"></span>
  <span class="abs social" style="left:981px"></span>
  <span class="abs social" style="left:1026px"></span>
  <span class="abs social" style="left:1071px"></span>
</footer>

</body>
</html>
```